The Vixen Rides Again Line of Sparkling Wine & Spirits

Back info: Tara Rose Whitfield Owner 209-555-0143 1480 E. Harlow Rd, Bldg. 7, & 8, Brightvale Ca. 95299
Sparkling Wines & Memorabilia www.thevixenridesagain.example
Ok I have uploaded the winning design. The color that I am after is the Fushia, Raspberry, Red, Matte Satin Matalic Finish. With a 24 Karet Gold color Foil. The Bottle is on the top row and it's the 2nd Bottle in. That is the Color that I want. This is the style of font. Make sure that you put what we're advertising. Good Luck to you all. Warmest regards, Tara
Target Market(s)
21 & up UniSex
Industry/Entity Type
Sparkling Wine and Memorabilia
Contact Information for Business Card
there listed up above.....

```html
<!DOCTYPE html>
<html lang="en">
<head>
<meta charset="utf-8">
<title>The Vixen Rides Again — Business Cards</title>
<link rel="stylesheet" href="https://fonts.googleapis.com/css2?family=Playfair+Display:wght@700&family=Poppins:wght@400;500&display=swap">
<style>
  :root {
    --backdrop: #2a2b2e;
    --fuchsia: #e0148f;
    --fuchsia-bright: #f0189c;
    --raspberry: #a8145f;
    --gold-light: #fbf0b8;
    --gold: #f0c560;
    --gold-deep: #d19f25;
    --ink: #111111;
    --paper-text: #ffffff;
  }
  * { box-sizing: border-box; margin: 0; padding: 0; }
  html, body { width: 1200px; height: 952px; overflow: hidden; }
  body {
    background: var(--backdrop);
    font-family: "Poppins", sans-serif;
    position: relative;
  }
  .card {
    position: absolute;
    left: 310px;
    width: 580px;
    height: 331px;
    border-radius: 4px;
    overflow: hidden;
    background: linear-gradient(135deg, var(--fuchsia-bright) 0%, var(--fuchsia) 45%, var(--raspberry) 100%);
    box-shadow: 0 18px 40px rgba(0,0,0,0.45);
  }
  .card--brand { top: 90px; }
  .card--contact { top: 531px; }

  /* Brand side */
  .gold-band {
    position: absolute;
    left: 0; right: 0;
    top: 72px;
    height: 187px;
    background: linear-gradient(120deg, var(--gold-light) 0%, var(--gold) 45%, var(--gold-deep) 100%);
    border-top: 3px solid var(--ink);
    border-bottom: 3px solid var(--ink);
    display: flex;
    align-items: center;
    justify-content: center;
  }
  .wordmark {
    font-family: "Playfair Display", serif;
    font-weight: 700;
    font-size: 44px;
    color: var(--ink);
    letter-spacing: 0.5px;
  }

  /* Contact side */
  .edge-strip {
    position: absolute;
    left: 34px;
    top: 0;
    width: 16px;
    height: 100%;
  }
  .edge-strip__gold {
    height: 58%;
    background: linear-gradient(180deg, var(--gold-deep), var(--gold-light) 40%, var(--gold) 70%, var(--gold-deep));
  }
  .edge-strip__black {
    height: 42%;
    margin-top: 6px;
    background: var(--ink);
  }
  .crest-slot {
    position: absolute;
    left: 82px;
    top: 40px;
    width: 150px;
    height: 150px;
    display: flex;
    flex-direction: column;
    align-items: center;
    justify-content: center;
    gap: 10px;
    text-align: center;
  }
  .crest-slot__mark {
    width: 34px; height: 34px;
    background: var(--ink);
  }
  .crest-slot__name {
    font-family: "Poppins", sans-serif;
    font-weight: 500;
    font-size: 15px;
    line-height: 1.2;
    color: var(--ink);
  }
  .identity {
    position: absolute;
    right: 36px;
    top: 40px;
    text-align: right;
  }
  .identity__name {
    font-family: "Playfair Display", serif;
    font-weight: 700;
    font-size: 34px;
    color: var(--gold);
    line-height: 1.1;
  }
  .identity__role {
    font-size: 17px;
    color: var(--ink);
    margin-top: 2px;
  }
  .contact-list {
    position: absolute;
    right: 36px;
    top: 146px;
    list-style: none;
    text-align: right;
    color: var(--paper-text);
    font-size: 13px;
    line-height: 1.35;
  }
  .contact-list li {
    display: flex;
    justify-content: flex-end;
    align-items: center;
    gap: 9px;
    margin-bottom: 7px;
  }
  .icon {
    width: 20px; height: 20px;
    border-radius: 4px;
    background: var(--ink);
    flex: none;
    display: flex; align-items: center; justify-content: center;
  }
  .icon svg { width: 12px; height: 12px; }
  .social-row {
    position: absolute;
    right: 36px;
    bottom: 24px;
    display: flex;
    align-items: center;
    gap: 9px;
  }
  .tagline {
    font-size: 10px;
    color: var(--paper-text);
  }
</style>
</head>
<body>

  <section class="card card--brand" aria-label="Business card, brand side">
    <div class="gold-band">
      <span class="wordmark">The Vixen Rides Again</span>
    </div>
  </section>

  <section class="card card--contact" aria-label="Business card, contact side">
    <div class="edge-strip">
      <div class="edge-strip__gold"></div>
      <div class="edge-strip__black"></div>
    </div>

    <div class="crest-slot">
      <div class="crest-slot__mark"></div>
      <div class="crest-slot__name">The Vixen<br>Rides Again</div>
    </div>

    <div class="identity">
      <div class="identity__name">Tara Rose Whitfield</div>
      <div class="identity__role">Owner</div>
    </div>

    <ul class="contact-list">
      <li>
        <span>1480 E. Harlow Rd, Bldg. 7, &amp; 8<br>Brightvale Ca. 95299</span>
        <span class="icon"><svg viewBox="0 0 12 12"><path d="M6 0.5a3.8 3.8 0 0 0-3.8 3.8C2.2 7.2 6 11.5 6 11.5s3.8-4.3 3.8-7.2A3.8 3.8 0 0 0 6 0.5z" fill="var(--gold)"/><circle cx="6" cy="4.3" r="1.4" fill="var(--ink)"/></svg></span>
      </li>
      <li>
        <span>555-555-0143</span>
        <span class="icon"><svg viewBox="0 0 12 12"><path d="M2.5 1l2 2.3-1 1.3a7 7 0 0 0 3.9 3.9l1.3-1 2.3 2-1.2 1.5C5 10.8 1.2 7 .9 2.2z" fill="var(--gold)"/></svg></span>
      </li>
      <li>
        <span>hello@thevixenridesagain.example</span>
        <span class="icon"><svg viewBox="0 0 12 12"><rect x="1" y="2.5" width="10" height="7" fill="var(--gold)"/><path d="M1 2.5l5 4 5-4" stroke="var(--ink)" stroke-width="1" fill="none"/></svg></span>
      </li>
      <li>
        <span>www.thevixenridesagain.example</span>
        <span class="icon"><svg viewBox="0 0 12 12"><path d="M3 1l6.5 5.2-3 .4 1.8 3.5-1.3.7-1.8-3.5L3 9.3z" fill="var(--gold)"/></svg></span>
      </li>
    </ul>

    <div class="social-row">
      <span class="tagline">Sparkling Wines &amp; Memorabilia</span>
      <span class="icon" aria-hidden="true"></span>
      <span class="icon" aria-hidden="true"></span>
    </div>
  </section>

</body>
</html>
```